Bakery looking for new Business cards

I have a new logo and now its time to upgrade our business cards.
e-mail - info@corwelbakehouse.com
www.corwelbakehouse.com
318-547-2096

418e Pell Creek rd. Larkfield IL 60492
Bakehouse Hours Wednesday-Sunday 7am-4pm

Industry/Entity Type

Bakery

Contact Information for Business Card

Hr's

Requirements
Must have
• Business information.
Nice to have
• would like to include a QR code for our website.

```html
<!DOCTYPE html>
<html lang="en">
<head>
<meta charset="utf-8">
<title>Corwel Bakehouse – Business Cards</title>
<link rel="stylesheet" href="https://fonts.googleapis.com/css2?family=Arimo:wght@400;500&display=swap">
<style>
  :root {
    --stage: #2b2926;
    --card: #ffffff;
    --ink: #111111;
    --gold: #e2a844;
    --shadow: rgba(0,0,0,0.45);
  }
  * { margin: 0; padding: 0; box-sizing: border-box; }
  html, body { width: 1200px; height: 1200px; overflow: hidden; }
  body {
    background: var(--stage);
    font-family: "Arimo", Arial, sans-serif;
    color: var(--ink);
    position: relative;
  }
  .card {
    position: absolute;
    left: 172px;
    width: 856px;
    height: 500px;
    background: var(--card);
    overflow: hidden;
    box-shadow: 0 6px 18px var(--shadow);
  }
  .card--front { top: 85px; }
  .card--back { top: 634px; }
  .swoosh { position: absolute; left: 0; top: 0; width: 856px; height: 500px; }

  .brand { position: absolute; display: flex; align-items: center; }
  .brand__dot { border-radius: 50%; background: var(--gold); flex: none; }
  .brand__name { font-weight: 400; color: var(--ink); white-space: nowrap; }

  .card--front .brand { left: 60px; top: 190px; gap: 14px; }
  .card--front .brand__dot { width: 34px; height: 34px; }
  .card--front .brand__name { font-size: 34px; }

  .card--back .brand { left: 0; right: 0; top: 170px; justify-content: center; gap: 22px; }
  .card--back .brand__dot { width: 60px; height: 60px; }
  .card--back .brand__name { font-size: 60px; }

  .owner {
    position: absolute; right: 66px; top: 72px;
    font-size: 37px; white-space: nowrap;
  }
  .owner__role { font-size: 21px; }

  .contact { position: absolute; right: 66px; list-style: none; font-size: 20px; }
  .contact li { display: flex; align-items: center; justify-content: flex-end; height: 32px; white-space: nowrap; }
  .contact svg { width: 16px; height: 16px; margin-left: 20px; flex: none; }
  .contact--lines { top: 158px; }
  .contact--place { top: 294px; }
  .contact .spacer { width: 16px; margin-left: 20px; flex: none; }
  .contact--place li { height: 35px; }
</style>
</head>
<body>

<section class="card card--front">
  <div class="brand">
    <span class="brand__dot"></span>
    <span class="brand__name">Corwel Bakehouse</span>
  </div>

  <p class="owner">Marcus Delane / <span class="owner__role">Owner</span></p>

  <ul class="contact contact--lines">
    <li>318-547-2096
      <svg viewBox="0 0 16 16"><path fill="#111" d="M3.5 1.5l2.5 0 1 3.5-1.8 1.2a8 8 0 0 0 4.6 4.6L11 9l3.5 1v2.5c0 1-1 2-2 2A11 11 0 0 1 1.5 3.5c0-1 1-2 2-2z"/></svg>
    </li>
    <li>info@corwelbakehouse.com
      <svg viewBox="0 0 16 16"><rect x="1" y="3" width="14" height="10" rx="1" fill="#111"/><path d="M1.5 3.5L8 9l6.5-5.5" stroke="#fff" stroke-width="1.3" fill="none"/></svg>
    </li>
    <li>www.corwelbakehouse.com
      <svg viewBox="0 0 16 16"><g fill="none" stroke="#111" stroke-width="1.4"><circle cx="8" cy="8" r="6.3"/><ellipse cx="8" cy="8" rx="2.8" ry="6.3"/><path d="M1.7 8h12.6M3 4.5h10M3 11.5h10"/></g></svg>
    </li>
  </ul>

  <ul class="contact contact--place">
    <li>418e Pell Creek rd. Larkfield IL 60492
      <svg viewBox="0 0 16 16"><path fill="#111" d="M8 0.8a5 5 0 0 0-5 5c0 3.8 5 9.4 5 9.4s5-5.6 5-9.4a5 5 0 0 0-5-5zm0 7a2 2 0 1 1 0-4 2 2 0 0 1 0 4z"/></svg>
    </li>
    <li>Bakehouse Hours Wednesday-Sunday 7am-4pm<span class="spacer"></span></li>
  </ul>

  <svg class="swoosh" viewBox="0 0 856 500" aria-hidden="true">
    <path d="M180 500 C 480 470, 760 445, 856 418 L856 500 Z" fill="var(--ink)"/>
    <path d="M0 500 C 300 455, 640 405, 800 402 C 866 401, 866 428, 830 436 C 660 470, 380 492, 180 500 Z" fill="var(--gold)"/>
  </svg>
</section>

<section class="card card--back">
  <div class="brand">
    <span class="brand__dot"></span>
    <span class="brand__name">Corwel Bakehouse</span>
  </div>

  <svg class="swoosh" viewBox="0 0 856 500" aria-hidden="true">
    <g transform="translate(856 0) scale(-1 1)">
      <path d="M180 500 C 480 470, 760 445, 856 418 L856 500 Z" fill="var(--ink)"/>
      <path d="M0 500 C 300 455, 640 405, 800 402 C 866 401, 866 428, 830 436 C 660 470, 380 492, 180 500 Z" fill="var(--gold)"/>
    </g>
  </svg>
</section>

</body>
</html>
```